LUSTRIA INC. is a new Fashion Stylist, Design Merchandiser, and consultant in the fashion industry

We need a logo design for a new Calgary, Alberta based company that is in the business of making over your image, wardrobe and style for both business and personal purposes.

Target Market(s)

Professional female and male business people looking for a new style or complete fashion makeover including clothes closet merchandising and makeover.

Contact Information for Business Card

Number of Pages Required

1 page

Font styles to use
Script

Colors
fac994
fbe7d2
fee3d4

Requirements
Must have
• Fashion Industry theme that is very elegant and colorful using gold/bronze/silver color themes.
Nice to have
• Incorporate the company name with the creative font to come up with the appropriate "logo"

```html
<!DOCTYPE html>
<html lang="en">
<head>
<meta charset="utf-8">
<title>Lustria Inc. — Business Card</title>
<link rel="stylesheet" href="https://fonts.googleapis.com/css2?family=Kaushan+Script&display=swap">
<style>
  :root {
    --backdrop: #e7e8e9;
    --card: #59595b;
    --gold: #fac994;
    --cream: #fbe7d2;
    --script: "Kaushan Script", cursive;
  }
  * { margin: 0; padding: 0; box-sizing: border-box; }
  html, body {
    width: 1200px;
    height: 927px;
    overflow: hidden;
    background: var(--backdrop);
  }
  .sheet {
    position: relative;
    width: 1200px;
    height: 927px;
  }
  .card {
    position: absolute;
    left: 284px;
    width: 632px;
    height: 361px;
    background: var(--card);
    border-radius: 16px;
  }
  .card--front { top: 71px; }
  .card--back  { top: 490px; }

  .card__brand {
    position: absolute;
    left: 0;
    right: 0;
    text-align: center;
    font-family: var(--script);
    font-weight: 400;
    color: var(--cream);
    letter-spacing: 1px;
  }
  .card--front .card__brand { top: 52px; font-size: 46px; line-height: 60px; }
  .card--back  .card__brand { top: 146px; font-size: 46px; line-height: 60px; }

  .card__name {
    position: absolute;
    top: 168px;
    left: 0;
    right: 0;
    text-align: center;
    font-family: var(--script);
    font-size: 25px;
    color: var(--gold);
    letter-spacing: 1px;
  }
  .card__role {
    position: absolute;
    top: 216px;
    left: 0;
    right: 0;
    text-align: center;
    font-family: var(--script);
    font-size: 15px;
    color: var(--cream);
    letter-spacing: 1px;
  }
  .card__phone {
    position: absolute;
    top: 253px;
    left: 0;
    right: 0;
    text-align: center;
    font-family: var(--script);
    font-size: 13px;
    color: var(--cream);
    letter-spacing: 1px;
  }
</style>
</head>
<body>
  <main class="sheet">
    <section class="card card--front">
      <div class="card__brand">LUSTRIA INC.</div>
      <h1 class="card__name">CELINE VANDERHOLT</h1>
      <p class="card__role">fashion stylist design merchandiser consultant</p>
      <p class="card__phone">403-555-0148</p>
    </section>
    <section class="card card--back">
      <div class="card__brand">LUSTRIA INC.</div>
    </section>
  </main>
</body>
</html>
```